Attention grabbing 6x9 postcard

We are looking to have an attention grabbing post card that be sent out to homeowners from our roofing company Olum Roofing. the concept is that on the front it will say something like (STOP THE KNOCKING!
Tired of roofers knocking on your door? Contact us because we value your time as much as you value the roof over your head."
Olum Roofing
OlumRoofing.com
877.612.OLUM
info@olumroofing.com

Please feel free to come up with something very creative. Once we pick the final design we will provide the copy.

```html
<!DOCTYPE html>
<html lang="en">
<head>
<meta charset="utf-8">
<title>Olum Roofing Postcard</title>
<link rel="stylesheet" href="https://fonts.googleapis.com/css2?family=Fira+Sans:wght@400;600;800&display=swap">
<style>
  :root {
    --page: #ece6d8;
    --card-white: #ffffff;
    --brand-gold: #e8a21f;
    --brand-amber: #e7a928;
    --ink: #2a2f38;
    --ink-soft: #5c6068;
    --line-gold: #e9b52c;
  }
  * { box-sizing: border-box; margin: 0; padding: 0; }
  html, body {
    width: 1200px; height: 903px; overflow: hidden;
    background: var(--page);
    font-family: "Fira Sans", Arial, sans-serif;
  }
  .stage {
    width: 1200px; height: 903px;
    display: flex; align-items: center; justify-content: center; gap: 50px;
  }
  .postcard {
    position: relative;
    width: 540px; height: 360px;
    box-shadow: 0 10px 30px rgba(60, 45, 10, 0.18);
    overflow: hidden;
  }
  .postcard--front { background: var(--card-white); }
  .postcard--back {
    background: var(--brand-amber);
    display: flex; flex-direction: column; align-items: center; justify-content: center; gap: 26px;
  }
  .frame-lines { position: absolute; inset: 0; }
  .headline {
    position: absolute; left: 34px; top: 34px;
    color: var(--brand-gold);
    font-weight: 800; font-size: 38px; line-height: 0.98; letter-spacing: 0.5px;
    text-transform: uppercase;
  }
  .subhead {
    position: absolute; left: 34px; top: 124px; width: 250px;
    color: var(--ink); font-weight: 600; font-size: 16px; line-height: 1.2;
  }
  .rule {
    position: absolute; left: 34px; top: 172px; width: 240px; height: 1.5px;
    background: var(--line-gold);
  }
  .pitch {
    position: absolute; left: 34px; top: 186px; width: 250px;
    color: var(--ink-soft); font-size: 12.5px; line-height: 1.4;
  }
  .pitch .call { color: var(--brand-gold); font-weight: 600; }
  .contact {
    position: absolute; left: 370px; top: 232px;
    list-style: none;
    color: var(--brand-gold); font-weight: 600; font-size: 13px; line-height: 1.75;
  }
  .brand-name {
    display: flex; align-items: center; gap: 12px;
    color: var(--ink); font-weight: 600; font-size: 30px; letter-spacing: 1px;
  }
  .brand-name .mark { width: 22px; height: 22px; background: var(--ink); }
  .web-address {
    color: var(--ink); font-weight: 400; font-size: 20px; letter-spacing: 2px;
  }
</style>
</head>
<body>
<main class="stage">
  <section class="postcard postcard--front">
    <svg class="frame-lines" width="540" height="360" viewBox="0 0 540 360" fill="none" stroke="#e9b52c" stroke-width="2">
      <polyline points="296,0 350,160 540,184"/>
      <polyline points="306,0 360,154 540,176"/>
      <polyline points="0,300 250,290 300,360"/>
      <polyline points="540,205 370,196 290,290"/>
    </svg>
    <h1 class="headline">Stop the<br>Knocking!</h1>
    <p class="subhead">Tired of roofers knocking on your door?</p>
    <div class="rule"></div>
    <p class="pitch"><span class="call">Contact us</span> because we value your time as much as you value the roof over your head.</p>
    <ul class="contact">
      <li>877.612.OLUM</li>
      <li>OlumRoofing.com</li>
      <li>info@olumroofing.com</li>
    </ul>
  </section>

  <section class="postcard postcard--back">
    <div class="brand-name"><span class="mark"></span>Olum Roofing</div>
    <p class="web-address">OLUMROOFING.COM</p>
  </section>
</main>
</body>
</html>
```